Package Storage Service

Ideas...

Business Name... "TUCK IT AT BRAMWOOD":
Store it,
Don’t Ship it;
4-LESS
Convenience, Quality, Service

Easy as ABC…
A. Contact Us 064-293-5527
B. We deliver
C. We pick-up & Store

LESS, is the new MORE

Box Size* (Approx) Weight Limit Price per Month
41 cm X 34 cm X 26 cm 10 Kilos 12 CHFs/per month
48 cm X 43 cm X 35 cm 25 Kilos 25 CHFs/per month

* Larger sizes and prices available upon request.

Contact: Tom /064-293-5527

These are only ideas for a small package storage service for local college students. The storage times are usually for 1 - 3 months.
I need a catchy, creative, colorful design for a new business.

This flyer will need to be printable in color. A-4 size or 8 1/2 " X 11".

Target Market(s)

Hotel Management students leaving their program for vacations for short terms. They return after vacation or after practical work experiences 4 study.

Industry/Entity Type

College

Requirements
Must have
• Prices, box sizes, catchy format.

Idea will forward to their address should they not return to the school; for a postage fee + 15.00 CHFs.

Contact information for the PICKUP and DELIVERY Service... see above.

Include a PICKUP AND DELIVERY Option in the flyer.
Nice to have
• Colorful boxes with a creative idea for someone to choose spending a little each month rather than a lot at one time. 25 CHFs rather than 125 CHFs.
Should not have
• Not too wordy.

```html
<!DOCTYPE html>
<html lang="en">
<head>
<meta charset="UTF-8">
<title>Tuck It at Bramwood – Package Storage</title>
<link href="https://fonts.googleapis.com/css2?family=Archivo+Black&family=Oswald:wght@500;700&family=Arimo:wght@700&display=swap" rel="stylesheet">
<style>
  :root {
    --navy: #1d2a3e;
    --banner: #e3d2b9;
    --tan: #dca681;
    --charcoal: #3a3a3c;
    --cream: #f6f0e8;
    --sand: #e9dccd;
    --taupe: #8b7b6e;
    --earth: #4b4039;
    --dark-earth: #3a302a;
    --gold: #d8b25a;
    --red: #c8201e;
    --ink: #111111;
    --white: #ffffff;
  }
  * { margin: 0; padding: 0; box-sizing: border-box; }
  html, body { width: 848px; height: 1200px; overflow: hidden; }
  body { background: var(--white); }
  .flyer {
    position: relative; width: 848px; height: 1200px; overflow: hidden;
    background: linear-gradient(100deg, var(--cream) 0%, var(--sand) 60%, #e2d3c2 100%);
    font-family: "Arimo", Arial, sans-serif;
  }
  .header-shapes { position: absolute; left: 0; top: 0; }
  .brand-main {
    position: absolute; left: 30px; top: 30px; color: var(--navy);
    font-family: "Archivo Black", sans-serif; font-size: 132px; line-height: 132px; letter-spacing: -2px;
  }
  .brand-sub {
    position: absolute; left: 32px; top: 160px; color: var(--navy);
    font-family: "Archivo Black", sans-serif; font-size: 34px; line-height: 40px; letter-spacing: 0.5px;
  }
  .tagline {
    position: absolute; left: 575px; top: 14px; width: 265px; text-align: center;
    font-family: "Oswald", sans-serif; font-weight: 700; font-size: 31px; line-height: 39px;
    color: var(--white); text-shadow: 2px 2px 3px rgba(0,0,0,0.45);
  }
  .headline {
    position: absolute; left: 110px; top: 268px;
    font-family: "Oswald", sans-serif; font-weight: 700; font-size: 80px; line-height: 1;
    color: var(--ink); letter-spacing: -1px;
  }
  .steps { position: absolute; left: 40px; top: 386px; list-style: none; }
  .steps li {
    display: flex; align-items: center; gap: 12px; height: 47px;
    font-size: 33px; font-weight: 700; color: var(--ink);
  }
  .steps svg { width: 34px; height: 34px; }
  .photo-mover {
    position: absolute; left: 540px; top: 362px; width: 308px; height: 466px;
    background: radial-gradient(ellipse at 40% 30%, #c9a57a 0%, #a88d72 40%, #5d5a5e 75%, #3e4552 100%);
    clip-path: polygon(0 0, 100% 0, 100% 100%, 170px 100%, 170px 230px, 0 230px);
  }
  .slogan {
    position: absolute; left: 32px; top: 596px;
    font-family: "Oswald", sans-serif; font-weight: 500; font-size: 46px; line-height: 1;
    color: var(--red);
  }
  .price-table {
    position: absolute; left: 32px; top: 656px; border-collapse: collapse;
    font-size: 22px; font-weight: 700; color: var(--ink);
  }
  .price-table td { padding: 0 9px 0 0; height: 35px; white-space: nowrap; }
  .lower-band { position: absolute; left: 0; top: 826px; width: 848px; height: 208px; background: var(--taupe); }
  .photo-box { position: absolute; }
  .photo-box.archive { left: 56px; top: 790px; width: 230px; height: 205px;
    background: linear-gradient(160deg, #d9b98c, #b48c5e); }
  .photo-box.closed { left: 356px; top: 800px; width: 200px; height: 200px;
    background: linear-gradient(160deg, #e0c194, #b99364); }
  .photo-box.open { left: 590px; top: 778px; width: 240px; height: 240px;
    background: linear-gradient(160deg, #ead3ad, #c4a070); }
  .footnote {
    position: absolute; left: 0; top: 1034px; width: 848px; height: 44px;
    background: linear-gradient(90deg, #d9d4cf, #f4f2ef 50%, #d9d4cf);
    text-align: center; font-size: 23px; font-weight: 700; line-height: 44px; color: var(--ink);
  }
  .footer { position: absolute; left: 0; top: 1078px; width: 848px; height: 122px; background: var(--earth); }
  .footer-shapes { position: absolute; left: 0; top: 0; }
  .pickup {
    position: absolute; left: 16px; top: 32px;
    font-family: "Oswald", sans-serif; font-weight: 700; font-size: 50px; line-height: 1;
    color: var(--gold); letter-spacing: 1px;
  }
  .call { position: absolute; left: 560px; top: 6px; width: 280px; text-align: center; color: var(--white); }
  .call-label { font-family: "Oswald", sans-serif; font-weight: 700; font-size: 46px; line-height: 54px; display: block; }
  .call-number { font-size: 33px; font-weight: 700; line-height: 44px; display: block; }
</style>
</head>
<body>
<div class="flyer">
  <svg class="header-shapes" width="848" height="270" viewBox="0 0 848 270">
    <polygon points="0,0 848,0 848,258 0,150" fill="var(--charcoal)"/>
    <polygon points="0,14 480,14 520,118 480,214 0,214" fill="var(--banner)"/>
    <polygon points="560,0 848,0 848,216 560,216 538,108" fill="var(--tan)"/>
  </svg>

  <div class="brand-main">TUCK</div>
  <div class="brand-sub">IT AT BRAMWOOD</div>

  <p class="tagline">Store it,<br>Don’t Ship it;<br>4-LESS<br>Convenience,<br>Quality, Service</p>

  <h1 class="headline">Easy as ABC...</h1>

  <ul class="steps">
    <li><svg viewBox="0 0 34 34"><rect x="3" y="9" width="22" height="22" fill="none" stroke="#222" stroke-width="2.5"/><path d="M8 19 L14 26 L31 4" fill="none" stroke="#222" stroke-width="4" stroke-linecap="round"/></svg>Contact Us 064-293-5527</li>
    <li><svg viewBox="0 0 34 34"><rect x="3" y="9" width="22" height="22" fill="none" stroke="#222" stroke-width="2.5"/><path d="M8 19 L14 26 L31 4" fill="none" stroke="#222" stroke-width="4" stroke-linecap="round"/></svg>We deliver</li>
    <li><svg viewBox="0 0 34 34"><rect x="3" y="9" width="22" height="22" fill="none" stroke="#222" stroke-width="2.5"/><path d="M8 19 L14 26 L31 4" fill="none" stroke="#222" stroke-width="4" stroke-linecap="round"/></svg>We pick-up &amp; Store</li>
  </ul>

  <div class="photo-mover" role="img" aria-label="Photo of a man carrying a cardboard box marked fragile"></div>

  <h2 class="slogan">LESS, is the new MORE</h2>

  <table class="price-table">
    <tr><td>Box Size* (Approx)</td><td>Weight Limit</td><td>Price per Month</td></tr>
    <tr><td>41 cm X 34 cm X 26 cm</td><td>10 Kilos</td><td>12 CHFs/per month</td></tr>
    <tr><td>48 cm X 43 cm X 35 cm</td><td>25 Kilos</td><td>25 CHFs/per month</td></tr>
  </table>

  <div class="lower-band"></div>
  <div class="photo-box archive" role="img" aria-label="Photo of a lidded cardboard archive box"></div>
  <div class="photo-box closed" role="img" aria-label="Photo of a closed cardboard box"></div>
  <div class="photo-box open" role="img" aria-label="Photo of an open cardboard box"></div>

  <p class="footnote">* Larger sizes and prices available upon request.</p>

  <footer class="footer">
    <svg class="footer-shapes" width="848" height="122" viewBox="0 0 848 122">
      <polygon points="0,14 520,14 490,108 0,108" fill="var(--dark-earth)"/>
    </svg>
    <p class="pickup">PICKUP AND DELIVER</p>
    <p class="call"><span class="call-label">Call</span><span class="call-number">064-293-5527</span></p>
  </footer>
</div>
</body>
</html>
```